Business Card Design Project

We are a commercial talent casting company, a very "now" company. We need a new business card that is both current, graphic and elegantly interesting. As we are a service business,
we need something that will attract the attention of new clients,
yet project a business that is 25 years old.

Industry/Entity Type

Business

Requirements
Must have
• 1. Logo - Nora Quillan Casting
2. Address - 47 Thornbury Street
New York, New York 10010
3. Phone - 212-738-4192
4. E-Mail - Casting@noraquillan.example

Nice to have
• Would like the card in black and white with the only accent
color being red.

```html
<!DOCTYPE html>
<html lang="en">
<head>
<meta charset="utf-8">
<title>Nora Quillan Casting — Business Card</title>
<link rel="stylesheet" href="https://fonts.googleapis.com/css2?family=Michroma&display=swap">
<style>
  :root {
    --bg-light: #f4f4f4;
    --bg-dark: #8a8a8a;
    --card-black: #111111;
    --card-black-hi: #2e2e2e;
    --red: #ee0c0c;
    --ink: #0a0a0a;
    --grey-type: #5f6266;
  }
  html, body {
    margin: 0;
    padding: 0;
    width: 1200px;
    height: 1194px;
    overflow: hidden;
  }
  .canvas {
    position: relative;
    width: 1200px;
    height: 1194px;
    background: radial-gradient(ellipse at 30% 45%, var(--bg-light) 0%, #c9c9c9 55%, var(--bg-dark) 100%);
    font-family: "Michroma", "Arial Black", sans-serif;
  }
  .artwork {
    position: absolute;
    inset: 0;
    width: 1200px;
    height: 1194px;
  }
  .type {
    position: absolute;
    margin: 0;
    line-height: 1;
    white-space: nowrap;
    font-weight: 400;
  }
  .front-name {
    left: 723px;
    transform: translateX(-50%);
    font-size: 44px;
    letter-spacing: 5px;
    text-align: center;
  }
  .front-name--first { top: 130px; color: var(--grey-type); }
  .front-name--last  { top: 194px; color: var(--grey-type); }
  .front-name--trade { top: 262px; color: var(--red); }
  .back-name {
    right: 50px;
    font-size: 29px;
    letter-spacing: 5px;
    color: var(--ink);
    text-align: right;
  }
  .back-name--line1 { top: 684px; }
  .back-name--line2 { top: 734px; }
  .contact {
    position: absolute;
    right: 91px;
    top: 1016px;
    margin: 0;
    font-style: normal;
    font-size: 17px;
    font-variant: small-caps;
    letter-spacing: 2px;
    line-height: 27.5px;
    color: var(--ink);
    text-align: right;
  }
  .contact span { display: block; white-space: nowrap; }
</style>
</head>
<body>
<div class="canvas">
  <svg class="artwork" viewBox="0 0 755 751" preserveAspectRatio="none" aria-hidden="true">
    <defs>
      <linearGradient id="front-fill" x1="0" y1="0" x2="1" y2="1">
        <stop offset="0" stop-color="var(--card-black)"/>
        <stop offset="1" stop-color="var(--card-black-hi)"/>
      </linearGradient>
    </defs>

    <g class="card card--front">
      <path d="M102,63 H582 V319 A45,45 0 0 1 537,364 H57 V108 A45,45 0 0 1 102,63 Z" fill="url(#front-fill)"/>
      <rect class="brand-square" x="92" y="203" width="140" height="130" fill="var(--red)"/>
    </g>

    <g class="card card--back">
      <path d="M252,418 H735 V673 A45,45 0 0 1 690,718 H207 V463 A45,45 0 0 1 252,418 Z" fill="var(--red)"/>
      <rect class="brand-square" x="233" y="555" width="139" height="130" fill="var(--ink)"/>
    </g>
  </svg>

  <h1 class="type front-name front-name--first">NORA</h1>
  <p class="type front-name front-name--last">QUILLAN</p>
  <p class="type front-name front-name--trade">CASTING</p>

  <p class="type back-name back-name--line1">NORA QUILLAN</p>
  <p class="type back-name back-name--line2">CASTING</p>

  <address class="contact">
    <span>47 Thornbury Street</span>
    <span>New York,&nbsp; 10010</span>
    <span>212-738-4192</span>
    <span>Casting@noraquillan.example</span>
  </address>
</div>
</body>
</html>
```